Business cards in digital learning for freelancer

Hello, I need a business cards in french. I work in the Digital learning industries as freeelancer; I'm an expert in digital learning. I work in France. My customer are in the health industry, pharmaceutical industry, and training organization. I've got a logo. I offer three services: consulting, Design, and Training. In the consulting, I offers coaching to choose your digital learning tools and the digital learning strategy. For the Design, I product differents level of elearning like rapid-learning, elearning, micro-learning, video-learning. And for the training service, I've create training about pedagogy, digital learning management project, Digital learning design.
I join my Logo create in this platform. My universe is gamified. I like the life, and I'm very social. I want a card like I'm I. I love Art (painting), Europeen comics. I use in my visual support "permanent maker" font and caracters. I would like cards: elegant, modern, Top class. If you need any information, you can ask me.
thanks for ideas

Target Market(s)

in health industries and training organization for Training manager, instructor, human resources director

Contact Information for Business Card

Phone number : 06 31 87 59 14 , mail: lucienmorvaltes@courriel-nord.fr, web: lucienmorvaltes.fr , LinkedIn

Font styles to use
Sans Serif

Requirements
Must have
• Use my logo and write my 3 services (consulting, training, design)

```html
<!DOCTYPE html>
<html lang="fr">
<head>
<meta charset="utf-8">
<title>Morvaltes – Cartes de visite</title>
<link rel="stylesheet" href="https://fonts.googleapis.com/css2?family=Arimo:wght@400;700&family=Montserrat:wght@500&display=swap">
<style>
  :root {
    --orange: #f07427;
    --white: #ffffff;
    --ink: #2b2b2b;
    --rule: #8a8a8a;
    --backdrop: #cfcfcf;
  }
  * { margin: 0; padding: 0; box-sizing: border-box; }
  html, body { width: 1200px; height: 915px; overflow: hidden; }
  body {
    background: var(--backdrop);
    font-family: "Arimo", Arial, sans-serif;
    position: relative;
  }
  .card {
    position: absolute;
    width: 570px;
    height: 326px;
    box-shadow: 0 10px 24px rgba(0,0,0,0.18);
    overflow: hidden;
  }

  /* Front */
  .card--front {
    left: 60px; top: 90px;
    background: var(--orange);
    color: var(--white);
  }
  .brand {
    position: absolute;
    display: flex;
    flex-direction: column;
    align-items: center;
  }
  .card--front .brand { left: 0; right: 0; top: 92px; }
  .brand__row { display: flex; align-items: center; gap: 12px; }
  .brand__dot {
    width: 30px; height: 30px;
    border-radius: 50%;
    background: currentColor;
  }
  .brand__name {
    font-weight: 700;
    font-size: 44px;
    letter-spacing: 2px;
  }
  .brand__tagline {
    margin-top: 6px;
    font-size: 13px;
    letter-spacing: 3px;
    text-transform: uppercase;
    padding: 0 18px;
    border-top: 1px solid currentColor;
    padding-top: 5px;
  }
  .services {
    position: absolute;
    left: 0; right: 0; top: 232px;
    display: flex;
    justify-content: center;
    gap: 34px;
    font-family: "Montserrat", Arial, sans-serif;
    font-weight: 500;
    font-size: 19px;
    letter-spacing: 3px;
    list-style: none;
  }
  .services li::before { content: "•"; margin-right: 6px; }

  /* Back */
  .card--back {
    left: 570px; top: 500px;
    background: var(--white);
    border-bottom: 14px solid var(--orange);
  }
  .card--back .brand {
    left: 34px; top: 64px;
    color: var(--orange);
    align-items: flex-start;
  }
  .card--back .brand__name { font-size: 30px; }
  .card--back .brand__dot { width: 22px; height: 22px; }
  .card--back .brand__tagline {
    font-size: 10px;
    color: var(--ink);
    border-color: var(--rule);
  }
  .person {
    position: absolute;
    right: 34px; top: 56px;
    text-align: right;
    padding-bottom: 8px;
    border-bottom: 1px solid var(--rule);
    width: 250px;
  }
  .person__name {
    color: var(--orange);
    font-weight: 700;
    font-size: 24px;
    letter-spacing: 0.5px;
  }
  .person__role { font-size: 15px; color: var(--ink); margin-top: 2px; }
  .contacts {
    position: absolute;
    left: 34px; top: 188px;
    width: 300px;
    padding-top: 10px;
    border-top: 1px solid var(--rule);
    list-style: none;
    font-size: 15px;
    color: var(--ink);
  }
  .contacts li { display: flex; align-items: center; gap: 8px; line-height: 23px; }
  .contacts svg { width: 14px; height: 14px; flex: none; }
</style>
</head>
<body>

<section class="card card--front" aria-label="Recto">
  <div class="brand">
    <div class="brand__row">
      <span class="brand__dot"></span>
      <span class="brand__name">MORVALTES</span>
    </div>
    <span class="brand__tagline">Digital Learning</span>
  </div>
  <ul class="services">
    <li>Consulting</li>
    <li>Training</li>
    <li>Design</li>
  </ul>
</section>

<section class="card card--back" aria-label="Verso">
  <div class="brand">
    <div class="brand__row">
      <span class="brand__dot"></span>
      <span class="brand__name">MORVALTES</span>
    </div>
    <span class="brand__tagline">Digital Learning</span>
  </div>

  <div class="person">
    <p class="person__name">LUCIEN MORVALTES</p>
    <p class="person__role">Creative Director</p>
  </div>

  <ul class="contacts">
    <li>
      <svg viewBox="0 0 24 24" aria-hidden="true"><path fill="var(--orange)" d="M6.6 10.8a15 15 0 0 0 6.6 6.6l2.2-2.2c.3-.3.7-.4 1-.2 1.1.4 2.3.6 3.6.6.6 0 1 .4 1 1V20c0 .6-.4 1-1 1A17 17 0 0 1 3 4c0-.6.4-1 1-1h3.5c.6 0 1 .4 1 1 0 1.3.2 2.5.6 3.6.1.3 0 .7-.2 1z"/></svg>
      06 31 87 59 14
    </li>
    <li>
      <svg viewBox="0 0 24 24" aria-hidden="true"><rect x="2" y="5" width="20" height="14" fill="var(--orange)"/><path d="M2 5l10 8 10-8" fill="none" stroke="#fff" stroke-width="2"/></svg>
      lucienmorvaltes@courriel-nord.fr
    </li>
    <li>
      <svg viewBox="0 0 24 24" aria-hidden="true"><circle cx="12" cy="12" r="10" fill="none" stroke="var(--orange)" stroke-width="2"/><path d="M2 12h20M12 2c3 3 3 17 0 20M12 2c-3 3-3 17 0 20" fill="none" stroke="var(--orange)" stroke-width="1.6"/></svg>
      www.lucienmorvaltes.fr
    </li>
    <li>
      <svg viewBox="0 0 24 24" aria-hidden="true"><circle cx="12" cy="12" r="10" fill="var(--orange)"/></svg>
      @lucienmorvaltes
    </li>
  </ul>
</section>

</body>
</html>
```